Plumvale CEO needs a Crowdsourced Graphic for a Wirelark Article

I need a simple graphic / banner for a blog post that's going to be posted on Wirelark (www.wirelark.com) - the biggest tech blog in the world.

The article will be written by Tobin Marsh (Plumvale's CEO) and the title will be "Asia's Secret Crowdsourcing Boom". The article is about the tens of thousands of people using crowdsourcing websites (like Plumvale.com, Qorvel.com and Vantrio.com) in China, India, the Philippines, Australia and other countries in the Asia Pacific region.

We'd really like to get this ASAP - so early submissions encouraged. We will try and get the winning designer linked to from the article.

Thanks to everyone that submitted!  Some great designs and hard to choose! :)

Target Market(s)

Tech saavy readers, English speakers

Industry/Entity Type

Tech

Requirements
Must have
• The graphic SHOULD:
1) Have the text "Asia's secret crowdsourcing boom" with some nice design and fonts (consider grey subtle pattern background and white drop shadow on fonts) - see attached examples
2) Have an Asian theme
3) Have the dimensions 640px wide by 240px wide
Nice to have
• The graphic COULD:
1) Have references to some or all of the countries mentioned above or use Asian characters as part of the background / motif (maybe the word "crowd" or "crowd sourcing" in different languages). In Chinese, the word for crowdsourcing is "witkey" (and there are corresponding Chinese characters: ??)
2) Emphasize the word "Asia" (using color and larger/different font)
3) Use a chart showing exponential (i.e. fast) growth - like the attached
4) Have a second line of text "5 Things You Didn't Know About Crowdsourcing in Asia"

```html
<!DOCTYPE html>
<html lang="en">
<head>
<meta charset="utf-8">
<title>Asia's Secret Crowdsourcing Boom</title>
<link rel="stylesheet" href="https://fonts.googleapis.com/css2?family=Anton&family=Oswald:wght@500&family=Noto+Serif+SC:wght@400&display=swap">
<style>
  :root {
    --bg-light: #f7f7f8;
    --bg-mid: #dcdcdf;
    --bg-edge: #c9c9cd;
    --glyph: #b9b5cf;
    --map-tone: #e6e6ee;
    --map-edge: #c7c6da;
    --accent: #5a2d91;
    --navy: #2a1f5c;
    --shadow: #ffffff;
  }
  html, body {
    margin: 0;
    padding: 0;
    width: 1200px;
    height: 450px;
    overflow: hidden;
  }
  .banner {
    position: relative;
    width: 1200px;
    height: 450px;
    overflow: hidden;
    background: radial-gradient(ellipse at 35% 45%, var(--bg-light) 0%, var(--bg-mid) 60%, var(--bg-edge) 100%);
  }
  .region-map {
    position: absolute;
    left: 110px;
    top: 10px;
    width: 270px;
    height: 430px;
    border-radius: 40% 45% 35% 50%;
    background: radial-gradient(ellipse at 50% 45%, var(--map-tone) 0%, rgba(230,230,238,0.6) 55%, rgba(230,230,238,0) 75%);
  }
  .backdrop-glyphs {
    position: absolute;
    left: 385px;
    top: -40px;
    margin: 0;
    font-family: "Noto Serif SC", serif;
    font-size: 410px;
    line-height: 1;
    letter-spacing: 0;
    color: var(--glyph);
    opacity: 0.75;
    white-space: nowrap;
  }
  .growth-line {
    position: absolute;
    inset: 0;
  }
  .headline {
    position: absolute;
    left: 165px;
    top: 124px;
    margin: 0;
    display: flex;
    align-items: baseline;
    gap: 30px;
    text-shadow: 2px 2px 0 var(--shadow), -1px -1px 0 var(--shadow);
  }
  .headline-emphasis {
    font-family: "Anton", sans-serif;
    font-size: 60px;
    line-height: 1;
    color: var(--accent);
    display: inline-flex;
    align-items: flex-start;
  }
  .headline-emphasis .apostrophe-arrow {
    width: 14px;
    height: 30px;
    margin: 2px 2px 0 3px;
  }
  .headline-rest {
    font-family: "Oswald", sans-serif;
    font-weight: 500;
    font-size: 40px;
    line-height: 1;
    color: var(--navy);
    letter-spacing: 0.5px;
  }
</style>
</head>
<body>
  <div class="banner">
    <div class="region-map" role="img" aria-label="Faint outline map of Asia and Australia"></div>

    <p class="backdrop-glyphs" lang="zh">众包</p>

    <svg class="growth-line" width="1200" height="450" viewBox="0 0 1200 450" aria-hidden="true">
      <polyline points="0,362 278,212 988,212 1128,0" fill="none" stroke="var(--accent)" stroke-width="4" stroke-linejoin="miter"/>
      <polygon points="262,208 249,236 240,220" fill="var(--accent)"/>
      <polygon points="1052,116 1048,146 1034,136" fill="var(--accent)"/>
    </svg>

    <h1 class="headline">
      <span class="headline-emphasis">ASIA<svg class="apostrophe-arrow" viewBox="0 0 14 30" aria-hidden="true"><polygon points="7,0 14,11 9,11 9,30 5,30 5,11 0,11" fill="var(--accent)"/></svg>S</span>
      <span class="headline-rest">SECRET CROWDSOURCING BOOM</span>
    </h1>
  </div>
</body>
</html>
```